Real Estate Virtual 360 Tour Web Home Page [Design Only]

see new upload mockup attached

We want new design ideas for our home page.

Link to video from web dev team of wireframe for reference: https://files.quorvantshare.net/d/7q-WpR2n8Lx4Tb6Hc0Yv9Ke3Mz5Ud/view?usp=sharing

Things desired on the home page:

Book a shoot now - Multiple markets,links to the corresponding market page for actual booking

1 Complete Package - includes Video, 3D Doviquell Tours, Exterior 360 Tours, Map, Agent Profile, Floor Plans, 2D Photos with blue sky and twilight sky guarantee

How it Works-https://clipnestra.net/582716049

Pricing-https://brisklumehomes.net/pricing/

House Search-https://brisklumehomes.net/

Footer
Updates

Target Market(s)

Real Estate Agents, Realtors, Home Buyers

Number of Pages Required

1 page

Font styles to use
Sans Serif

Colors
0555a3

Requirements
Must have
• see new upload mockup attached

Footer

```html
<!DOCTYPE html>
<html lang="en">
<head>
<meta charset="utf-8">
<title>Brisklume Homes – Home</title>
<link href="https://fonts.googleapis.com/css2?family=Roboto:wght@400;500;700&display=swap" rel="stylesheet">
<style>
:root{
  --blue:#30619f;
  --blue-dark:#27538c;
  --ink:#2c5a97;
  --text:#6d7480;
  --muted:#9aa1ab;
  --light:#eef2f8;
  --grey:#f4f4f5;
  --line:#dfe3e8;
  --gold:#f2b705;
  --red:#e8473a;
  --white:#fff;
}
*{box-sizing:border-box;margin:0;padding:0}
html,body{width:1200px;height:5021px;overflow:hidden}
body{font-family:"Roboto",Arial,sans-serif;color:var(--text);background:var(--white);position:relative}
.abs{position:absolute}
a{color:inherit;text-decoration:none}
.btn{position:absolute;background:var(--blue);color:#fff;font-weight:700;font-size:14px;border-radius:26px;display:flex;align-items:center;justify-content:center;letter-spacing:.3px}
.btn-sq{border-radius:4px}
.ph{position:absolute}
.h2{color:var(--ink);font-weight:500}
p{line-height:26px;font-size:13.5px}

/* top bar */
.topbar{left:0;top:0;width:1200px;height:45px;background:var(--blue);color:#fff;font-size:14px;font-weight:500}
.topbar .phone{left:108px;top:13px;display:flex;gap:6px;align-items:center}
.topbar .social{right:108px;top:16px;display:flex;gap:12px}
.dot{width:13px;height:13px;border-radius:50%;background:rgba(255,255,255,.85)}
/* header */
.brand{left:108px;top:72px;font-size:26px;font-weight:700;color:var(--ink);display:flex;align-items:center;gap:10px}
.brand .mark{width:18px;height:18px;background:var(--ink)}
.nav{left:465px;top:92px;display:flex;gap:38px;font-size:14.5px;color:#222;font-weight:500}
.nav .on{color:var(--ink)}
/* hero */
.hero-img{left:0;top:155px;width:793px;height:565px;background:linear-gradient(180deg,#b7cde4 0%,#a9a79f 45%,#7f8a62 85%,#6f7c47 100%)}
.hero-card{left:662px;top:378px;width:538px;height:277px;background:#fff}
.hero-card h1{position:absolute;left:41px;top:36px;width:460px;font-size:34px;line-height:42px;color:var(--ink);font-weight:500}
/* about */
.about{left:0;top:720px;width:453px;height:544px;background:var(--light)}
.about h2{position:absolute;left:58px;top:60px;width:360px;font-size:32px;line-height:44px}
.about p{position:absolute;left:58px;width:340px}
.grid{left:453px;top:720px;width:747px;height:544px;display:grid;grid-template-columns:repeat(3,1fr);grid-template-rows:repeat(3,1fr);gap:2px;background:#fff}
.grid div:nth-child(3n+1){background:linear-gradient(#b9cbe0,#8d7c6a)}
.grid div:nth-child(3n+2){background:linear-gradient(#a9c3e2,#6a7f90)}
.grid div:nth-child(3n){background:linear-gradient(#c7d8ea,#a49a76)}
/* how it works */
.how-box{left:111px;top:1361px;width:475px;height:451px;background:var(--blue);color:#fff;text-align:center}
.how-box .avatar{position:absolute;left:196px;top:126px;width:84px;height:84px;border-radius:50%;background:#fff}
.how-box .avatar::after{content:"";position:absolute;left:25px;top:14px;width:34px;height:34px;border-radius:50%;background:var(--blue)}
.how-box .avatar::before{content:"";position:absolute;left:16px;top:52px;width:52px;height:22px;border-radius:26px 26px 6px 6px;background:var(--blue)}
.how-box p{position:absolute;left:70px;top:228px;width:335px;font-style:italic;font-size:15px}
.how-text{left:632px;top:1352px;width:450px}
.how-text h2{font-size:36px;margin-bottom:16px}
.quote{left:632px;top:1597px;width:52px;height:52px;border-radius:50%;background:var(--light);color:var(--ink);font-size:28px;font-weight:700;text-align:center;line-height:60px}
.how-quote{left:632px;top:1658px;width:440px;font-style:italic;font-size:12.5px;line-height:26px}
/* search */
.search-img{left:0;top:1907px;width:322px;height:313px;background:linear-gradient(90deg,#8aa3bb,#c8d3dd 35%,#9a5b4a 55%,#6d7e94 80%,#a5b4c4)}
.search{left:322px;top:1907px;width:878px;height:313px;background:var(--grey)}
.lbl{position:absolute;font-size:13px;font-weight:700;color:var(--ink)}
.fld{position:absolute;height:44px;background:#fff;border:1px solid var(--line);font-size:12px;color:#777;padding:0 18px;display:flex;align-items:center;justify-content:space-between}
/* listings */
.card{position:absolute;width:310px;height:340px;background:#fff;box-shadow:0 2px 10px rgba(0,0,0,.13)}
.card .img{position:absolute;left:7px;top:7px;width:296px;height:210px;background:linear-gradient(180deg,#b5c8dd 0%,#8996a3 55%,#7c7d5e 100%)}
.tag{position:absolute;left:15px;top:21px;background:var(--red);color:#fff;font-size:12px;font-weight:700;padding:6px 10px}
.card h3{position:absolute;left:27px;top:232px;width:260px;font-size:17px;line-height:25px;color:var(--ink);font-weight:500}
.card .price{position:absolute;left:27px;top:286px;font-size:25px;color:#777;font-weight:500}
/* map */
.map{left:0;top:3120px;width:1200px;height:385px;background:linear-gradient(135deg,#e8ebe4,#dfe5da 40%,#eceeea)}
/* pricing */
.pricing h2{position:absolute;left:0;top:3586px;width:1200px;text-align:center;font-size:37px}
.pricing .lead{position:absolute;left:190px;top:3650px;width:820px;text-align:center}
.plan{position:absolute;top:3770px;width:306px;height:370px;background:#fff;box-shadow:0 2px 12px rgba(0,0,0,.12);text-align:center}
.plan .head{position:absolute;left:15px;top:20px;width:276px;height:52px;border-bottom:1px solid var(--line);display:flex;align-items:center;justify-content:center;gap:6px;font-size:13px}
.plan .head b{font-size:33px;color:var(--gold);font-weight:700}
.plan p{position:absolute;left:30px;top:96px;width:246px;color:#b0b5bc;font-size:13.5px}
/* team */
.team h2{position:absolute;left:110px;top:4212px;font-size:35px}
.team p{position:absolute;left:110px;width:486px}
.people{left:600px;top:4235px;width:492px;height:306px;display:grid;grid-template-columns:repeat(3,152px);grid-template-rows:repeat(2,152px);gap:2px 18px}
.people div{background:linear-gradient(180deg,#e9e3da,#c9b7a3)}
.people .hl{background:#4f7cb6;color:#fff;text-align:center;font-weight:700;font-size:14px;padding-top:54px}
/* footer */
.footer{left:0;top:4650px;width:1200px;height:371px;background:var(--blue);color:#fff}
.footer h4{position:absolute;top:80px;font-size:18px;font-weight:700}
.footer ul{position:absolute;list-style:none;font-size:14px;line-height:31px}
.footer li::before{content:"»";margin-right:14px}
.ci{position:absolute;left:403px;font-size:14px;line-height:28px;display:flex;gap:18px}
.sub-in{left:752px;top:4811px;width:246px;height:42px;background:#fff;color:#8a8f96;font-size:14px;padding:12px 22px}
.sub-btn{left:752px;top:4870px;width:118px;height:40px;background:#222;color:#fff;font-size:13px;font-weight:700;display:flex;align-items:center;justify-content:center}
.fsoc{left:937px;top:4938px;display:flex;gap:12px}
.fsoc span{width:40px;height:40px;border-radius:50%;background:#2d2d2d;display:flex;align-items:center;justify-content:center}
.fsoc span i{width:12px;height:12px;border-radius:50%;background:#fff}
</style>
</head>
<body>

<header>
  <div class="abs topbar">
    <div class="abs phone"><svg width="13" height="13" viewBox="0 0 24 24" fill="#fff"><path d="M6.6 10.8a15.1 15.1 0 0 0 6.6 6.6l2.2-2.2c.3-.3.7-.4 1-.2 1.1.4 2.3.6 3.6.6.6 0 1 .4 1 1V20c0 .6-.4 1-1 1A17 17 0 0 1 3 4c0-.6.4-1 1-1h3.5c.6 0 1 .4 1 1 0 1.3.2 2.5.6 3.6.1.3 0 .7-.2 1z"/></svg>555-014-2290</div>
    <div class="abs social"><span class="dot"></span><span class="dot"></span><span class="dot"></span></div>
  </div>
  <div class="abs brand"><span class="mark"></span>Brisklume Homes</div>
  <nav class="abs nav"><a class="on">Home</a><a>About us</a><a>Property</a><a>Blog</a><a>Contact us</a></nav>
  <a class="btn" style="left:953px;top:78px;width:135px;height:50px">GET A QUOTE</a>
</header>

<section class="hero">
  <div class="ph hero-img" role="img" aria-label="Photo of a two-storey suburban house with a garage and lawn"></div>
  <div class="abs hero-card">
    <h1>Lorem ipsum dolor sit amet, consectetur adipiscing elit sed do eiusmod</h1>
    <a class="btn" style="left:41px;top:175px;width:162px;height:52px">GET STARTED</a>
  </div>
</section>

<section>
  <div class="abs about">
    <h2 class="h2">Lorem ipsum dolor sit amet, consectetur</h2>
    <p style="top:164px">Lorem ipsum dolor sit amet, consectetur adipiscing elit, sed do eiusmod tempor incididunt ut labore et dolore magna aliqua. Ut enim ad minim veniam, quis nostrud exercitation ullamco laboris nisi ut aliquip ex ea commodo consequat. Duis aute irure dolor in reprehenderit in voluptate velit esse cillum dolore eu fugiat nulla pariatur</p>
    <p style="top:370px">Lorem ipsum dolor sit amet, consectetur adipiscing elit, sed do eiusmod tempor incididunt ut labore et dolore magna aliqua. Ut enim ad minim veniam, quis nostrud exercitation ullamco laboris nisi ut aliquip ex ea commodo consequat.</p>
  </div>
  <div class="abs grid" role="img" aria-label="Grid of nine property and neighbourhood photos">
    <div></div><div></div><div></div><div></div><div></div><div></div><div></div><div></div><div></div>
  </div>
</section>

<section>
  <div class="abs how-box" role="img" aria-label="Faded photo of a building behind a profile card">
    <div class="avatar"></div>
    <p>Lorem ipsum dolor sit amet, consectetur adipiscing elit, sed do eiusmod tempor incididunt ut labore et dolore magna aliqua. Ut enim ad minim veniam</p>
  </div>
  <div class="abs how-text">
    <h2 class="h2">How it works</h2>
    <p style="font-size:13px">Lorem ipsum dolor sit amet, consectetur adipiscing elit, sed do eiusmod tempor incididunt ut labore et dolore magna aliqua. Ut enim ad minim veniam, quis nostrud exercitation ullamco laboris nisi ut aliquip ex ea commodo consequat. Duis aute irure dolor in reprehenderit in voluptate velit esse cillum dolore eu fugiat nulla pariatur</p>
  </div>
  <div class="abs quote">“</div>
  <p class="abs how-quote">"Lorem ipsum dolor sit amet, consectetur adipiscing elit, sed do eiusmod tempor incididunt ut labore et dolore magna aliqua. Ut enim ad minim veniam, quis nostrud exercitation ullamco laboris nisi ut aliquip ex ea commodo consequat.Lorem ipsum dolor sit amet, consectetur adipiscing elit, sed do eiusmod tempor incididunt ut labore et dolore magna aliqua. Ut enim ad minim veniam, quis "</p>
</section>

<section>
  <div class="ph search-img" role="img" aria-label="Collage of local storefront and street photos"></div>
  <div class="abs search">
    <span class="lbl" style="left:54px;top:27px">Cities</span>
    <span class="lbl" style="left:302px;top:27px">Price Max</span>
    <span class="lbl" style="left:415px;top:27px">Price Max</span>
    <span class="lbl" style="left:528px;top:27px">Min Bedrooms:</span>
    <span class="lbl" style="left:665px;top:27px">Min Bathrooms:</span>
    <div class="fld" style="left:54px;top:60px;width:240px">Select city<span>▾</span></div>
    <div class="fld" style="left:302px;top:60px;width:105px"></div>
    <div class="fld" style="left:415px;top:60px;width:105px"></div>
    <div class="fld" style="left:528px;top:60px;width:130px"></div>
    <div class="fld" style="left:665px;top:60px;width:130px"></div>
    <span class="lbl" style="left:54px;top:137px">Property types:</span>
    <span class="lbl" style="left:405px;top:137px">Show houses within</span>
    <span class="lbl" style="left:553px;top:137px">Property types:</span>
    <div class="fld" style="left:54px;top:170px;width:240px">for rent and for sale<span>▾</span></div>
    <span class="abs" style="left:302px;top:178px;font-size:10px">Garage</span>
    <span class="abs" style="left:348px;top:178px;font-size:10px">Basement</span>
    <span class="abs" style="left:316px;top:196px;width:9px;height:9px;border:1px solid #888"></span>
    <span class="abs" style="left:370px;top:196px;width:9px;height:9px;border:1px solid #888"></span>
    <div class="fld" style="left:403px;top:170px;width:50px;padding:0 14px">20</div>
    <div class="fld" style="left:460px;top:170px;width:50px;padding:0 14px">min</div>
    <span class="abs" style="left:525px;top:184px;font-size:12px">of</span>
    <div class="fld" style="left:553px;top:170px;width:242px">Enter a Location</div>
    <a class="btn" style="left:54px;top:245px;width:163px;height:46px">SEARCH</a>
  </div>
</section>

<section>
  <div class="card" style="left:111px;top:2315px"><div class="img" role="img" aria-label="Photo of a blue-sided townhouse"></div><span class="tag">FOR SALE</span><h3>1720 Quillon St Unit E Harlow, CO 80901</h3><span class="price">$31,000</span></div>
  <div class="card" style="left:445px;top:2315px"><div class="img" role="img" aria-label="Photo of a wooden cabin in snow"></div><span class="tag">FOR SALE</span><h3>4410 Upper Fenn Rd Pinecrest, CO 80902</h3><span class="price">$31,000</span></div>
  <div class="card" style="left:779px;top:2315px"><div class="img" role="img" aria-label="Photo of a single-storey house with carport"></div><span class="tag">FOR SALE</span><h3>3308 Ostrel St Commerce Vale, CO 80903</h3><span class="price">$295000</span></div>
  <div class="card" style="left:111px;top:2683px"><div class="img" role="img" aria-label="Photo of a row of townhouses with porch"></div><span class="tag">FOR SALE</span><h3>2915 Verano Ave Lindell, CO 80904</h3><span class="price">$31,000</span></div>
  <div class="card" style="left:445px;top:2683px"><div class="img" role="img" aria-label="Photo of a cottage among snowy trees"></div><span class="tag">FOR SALE</span><h3>612 Cobble Ave Marwick, CO 80905</h3><span class="price">$31,000</span></div>
  <div class="card" style="left:779px;top:2683px"><div class="img" role="img" aria-label="Photo of a two-storey house with garage"></div><span class="tag">FOR SALE</span><h3>1058 Talloway St Brenton, CO 80906</h3><span class="price">$31,000</span></div>
</section>

<div class="ph map" role="img" aria-label="Regional map showing property locations"></div>

<section class="pricing">
  <h2 class="h2">Our Pricing Plan</h2>
  <p class="lead">Lorem ipsum dolor sit amet, consectetur adipiscing elit, sed do eiusmod tempor incididunt ut labore et dolore magna aliqua. Ut enim ad minim veniam, quis nostrud exercitation ullamco laboris nisi ut aliquip ex ea commodo consequat. Duis aute irure dolor in reprehenderit in voluptate velit esse cillum dolore eu fugiat nulla pariatur</p>
  <div class="plan" style="left:114px"><div class="head">10 days - <b>$45</b> per card</div><p>Lorem ipsum dolor sit amet, consectetur adipiscing elit, sed do eiusmod tempor incididunt ut labore et dolore magna aliqua. Ut enim ad minim veniam, quis nostrud exercitation ullamco</p><a class="btn btn-sq" style="left:82px;top:280px;width:142px;height:48px">LEARN MORE</a></div>
  <div class="plan" style="left:447px"><div class="head">2 days - <b>$130</b> per card</div><p>Lorem ipsum dolor sit amet, consectetur adipiscing elit, sed do eiusmod tempor incididunt ut labore et dolore magna aliqua. Ut enim ad minim veniam, quis nostrud exercitation ullamco</p><a class="btn btn-sq" style="left:82px;top:280px;width:142px;height:48px">LEARN MORE</a></div>
  <div class="plan" style="left:780px"><div class="head">2 days - <b>$130</b> per card</div><p>Lorem ipsum dolor sit amet, consectetur adipiscing elit, sed do eiusmod tempor incididunt ut labore et dolore magna aliqua. Ut enim ad minim veniam, quis nostrud exercitation ullamco</p><a class="btn btn-sq" style="left:82px;top:280px;width:142px;height:48px">LEARN MORE</a></div>
</section>

<section class="team">
  <h2 class="h2">Our Team</h2>
  <p style="top:4270px">Lorem ipsum dolor sit amet, consectetur adipiscing elit, sed do eiusmod tempor incididunt ut labore et dolore magna aliqua. Ut enim ad minim veniam, quis nostrud exercitation ullamco laboris nisi ut aliquip ex ea commodo consequat. Duis aute irure dolor in reprehenderit in voluptate velit esse cillum dolore eu fugiat nulla pariatur</p>
  <p style="top:4425px">Lorem ipsum dolor sit amet, consectetur adipiscing elit, sed do eiusmod tempor incididunt ut labore et dolore magna aliqua. Ut enim ad minim veniam, quis nostrud exercitation ullamco laboris nisi ut aliquip ex ea commodo consequat. Duis aute irure dolor in reprehenderit in voluptate velit esse cillum dolore eu fugiat nulla pariatur</p>
  <div class="abs people">
    <div role="img" aria-label="Team member portrait"></div>
    <div class="hl" role="img" aria-label="Team member portrait with name overlay">John Doe</div>
    <div role="img" aria-label="Team member portrait"></div>
    <div role="img" aria-label="Team member portrait"></div>
    <div role="img" aria-label="Team member portrait"></div>
    <div role="img" aria-label="Team member portrait"></div>
  </div>
</section>

<footer class="abs footer">
  <h4 style="left:110px">QUICK LINKS</h4>
  <ul style="left:110px;top:125px"><li>Home</li><li>About us</li><li>Contact us</li><li>Privacy policy</li></ul>
  <h4 style="left:403px">CONTACT US</h4>
  <div class="ci" style="top:126px"><span>●</span><span>418 Marlow Ct Fairhaven, CO<br>80599</span></div>
  <div class="ci" style="top:198px"><span>✆</span><span>555-014-2290</span></div>
  <div class="ci" style="top:232px"><span>✉</span><span>hello@brisklumehomes.net</span></div>
  <h4 style="left:747px">SUBSCRIBE THE NEWSLETTER</h4>
  <span class="abs" style="left:749px;top:130px;font-size:13.5px">Lorem ipsum dolor sit amet, consectetur adipiscing</span>
  <span class="abs" style="left:110px;top:304px;font-size:14px">© Copyrights 2020 | Company name</span>
</footer>
<div class="abs sub-in">Email Address</div>
<div class="abs sub-btn">SUBSCRIBE</div>
<div class="abs fsoc"><span><i></i></span><span><i></i></span><span><i></i></span></div>

</body>
</html>
```